KTR Engineering Business Card Design

We’re looking for an elegant, clean, and timeless business card design that communicates experience, capability, and reliability.

KTR Engineering was established in 1995 , we are a Government Contracting company providing Professional Services to the Ministry of Harbor Works, Frontier Stewardship and the Waypoint Consortium. Our capabilities include: Acquisition & Program Management; Intelligence & Security Operations; Cyber, IT & Network Operations; Lifecycle Logistics & Asset Readiness; C5ISR Systems Engineering & Sustainment.

We want the card to reflect a straightforward, confident approach to business. The design should feel polished and professional without being flashy or overly corporate.

Design Direction
Clean, sophisticated, and uncluttered
Elegant but understated
Strong typography and thoughtful spacing
A timeless aesthetic rather than something overly trendy
Confident and established, with a sense of substance
Easy to read and practical in a real-world business setting

The overall impression should be: “These are experienced professionals who know what they’re doing, do what they say, and can be relied upon.”

We’re open to creative interpretations. The finished card should feel distinctive through its typography, proportions, layout, and attention to detail rather than through excessive graphics or visual effects.

We’re looking for a design that would make a potential client immediately feel that they’re dealing with a capable, trustworthy, and established company.

Company Colors: Navy and Gold/Yellow (but you do not need to use these colors on the card)
Company Name: KTR Engineering Associates, Inc. (known as KTR Engineering)
Website: ktrengineering.example
Company Logo: Navy & Gold (other variations attached)

```html
<!DOCTYPE html>
<html lang="en">
<head>
<meta charset="utf-8">
<title>KTR Engineering Business Card</title>
<link rel="stylesheet" href="https://fonts.googleapis.com/css2?family=Montserrat:wght@400;700;800&family=Lato:wght@400&display=swap">
<style>
  :root {
    --navy: #222c5f;
    --navy-deep: #1d2750;
    --gold: #fde14e;
    --ink: #141414;
    --muted: #3a3a3a;
    --paper: #ffffff;
    --backdrop: #9b9b9b;
  }
  html, body {
    margin: 0;
    padding: 0;
    width: 1200px;
    height: 1059px;
    overflow: hidden;
    background: var(--backdrop);
  }
  .canvas { position: relative; width: 1200px; height: 1059px; }

  .card {
    position: absolute;
    border-radius: 24px;
    overflow: hidden;
  }
  .card--front {
    left: 258px; top: 83px; width: 704px; height: 402px;
    background: var(--paper);
  }
  .card--back {
    left: 254px; top: 560px; width: 714px; height: 407px;
    background: var(--navy);
  }

  .wordmark {
    position: absolute;
    margin: 0;
    font-family: "Montserrat", sans-serif;
    font-weight: 800;
    letter-spacing: -2px;
    line-height: 1;
  }
  .card--front .wordmark {
    left: 405px; top: 60px;
    font-size: 100px;
    color: var(--navy);
  }
  .card--back .wordmark {
    left: 0; right: 0; top: 156px;
    text-align: center;
    font-size: 124px;
    color: var(--paper);
  }

  .holder-name {
    position: absolute; left: 44px; top: 199px; margin: 0;
    font-family: "Montserrat", sans-serif; font-weight: 700;
    font-size: 29px; color: var(--navy); letter-spacing: 0.5px;
    line-height: 1;
  }
  .holder-title {
    position: absolute; left: 43px; top: 236px; margin: 0;
    font-family: "Montserrat", sans-serif; font-weight: 400;
    font-size: 20px; color: var(--ink); letter-spacing: 0.5px;
    line-height: 1;
  }
  .divider {
    position: absolute; left: 48px; top: 268px; width: 620px; height: 1.5px;
    background: var(--ink);
  }

  .contact-list {
    position: absolute; left: 45px; top: 283px; margin: 0; padding: 0;
    list-style: none;
    font-family: "Lato", sans-serif; font-size: 17px; color: var(--ink);
  }
  .contact-item { display: flex; align-items: center; height: 28px; }
  .contact-item + .contact-item { margin-top: 0; }
  .contact-item--web { font-size: 19px; color: var(--muted); }
  .contact-icon { width: 22px; height: 22px; margin-right: 14px; flex: none; }

  .address {
    position: absolute; right: 36px; top: 316px; margin: 0;
    font-family: "Lato", sans-serif; font-style: normal; font-size: 16.5px;
    color: var(--ink); text-align: right; line-height: 20px;
  }

  .base-band { position: absolute; left: 0; bottom: 0; width: 100%; height: 15px; }
  .card--back .base-band { height: 14px; }
</style>
</head>
<body>
<main class="canvas">

  <section class="card card--front" aria-label="Business card front">
    <p class="wordmark">KTR</p>

    <h1 class="holder-name">MARCUS ELLERY</h1>
    <p class="holder-title">MANAGING DIRECTOR</p>
    <div class="divider"></div>

    <ul class="contact-list">
      <li class="contact-item">
        <svg class="contact-icon" viewBox="0 0 24 24" aria-hidden="true">
          <path fill="var(--navy)" d="M6.6 3.5l3 3.2-1.7 2.1c1.2 2.6 3.2 4.6 5.8 5.8l2.1-1.7 3.2 3-1.6 3.4c-7.8-.3-14.1-6.6-14.4-14.4z"/>
          <path fill="none" stroke="var(--navy)" stroke-width="1.6" d="M14 3.5a7 7 0 0 1 6.5 6.5M13.6 7a3.6 3.6 0 0 1 3.4 3.4"/>
        </svg>
        <span>055-987 210 346</span>
      </li>
      <li class="contact-item">
        <svg class="contact-icon" viewBox="0 0 24 24" aria-hidden="true">
          <rect x="1" y="5" width="22" height="15" fill="var(--navy)"/>
          <path d="M1.5 5.5L12 13.5l10.5-8" fill="none" stroke="var(--paper)" stroke-width="2"/>
        </svg>
        <span>hello@ktrmail.example</span>
      </li>
      <li class="contact-item contact-item--web">
        <svg class="contact-icon" viewBox="0 0 24 24" aria-hidden="true">
          <circle cx="12" cy="12" r="10" fill="var(--navy)"/>
          <path fill="var(--paper)" d="M7 6c2 0 3 1 2.5 2.5S7 10 8 12s1 3 0 4-3 0-4-2c0-3 1-6 3-8zm8 1c2 0 4 2 4 4s-2 2-3 1-2 1-1 3 0 4-1 4-2-2-2-4 2-3 1-5 0-3 2-3z"/>
        </svg>
        <span>ktrengineering.example</span>
      </li>
    </ul>

    <address class="address">718, Harborview Lane East<br>30917, Eastmarch</address>

    <svg class="base-band" viewBox="0 0 704 15" preserveAspectRatio="none" aria-hidden="true">
      <polygon points="0,0 360,0 333,15 0,15" fill="var(--navy)"/>
      <polygon points="371,0 704,0 704,15 345,15" fill="var(--gold)"/>
    </svg>
  </section>

  <section class="card card--back" aria-label="Business card back">
    <p class="wordmark">KTR</p>
    <svg class="base-band" viewBox="0 0 714 14" preserveAspectRatio="none" aria-hidden="true">
      <polygon points="0,0 372,0 345,14 0,14" fill="var(--navy-deep)"/>
      <polygon points="380,0 714,0 714,14 353,14" fill="var(--navy-deep)"/>
    </svg>
  </section>

</main>
</body>
</html>
```